"The Craft of Patron Care," fourth edition cover design

Later this year, my publisher, Harold Penmarsh & Daughters, will issue a fourth, substantially revised edition of "The Craft of Patron Care," following the 2016 publication of the third edition and the second and first versions that were issued earlier.

To distinguish this new edition from previous ones, I need a cover design that visually connects and is consistent with what has preceded it, while signaling this is a new and different, worthy of prospective readers/buyers’ attention.

Attached are three different verbal approaches to the new cover; these are NOT MEANT to serve as actual designs, but rather will give you a sense of how language is to be deployed:

The first emphasizes “ART” as the key visual word in the book title;
The second emphasizes “CLIENT SERVICE” as the key visual words in the book title; and,
The third emphasizes just the word "CLIENT" in the book title.

A top-of-the-page is a pre-head that applies to all three versions:
“6 TIMELESS PRINCIPLES FOR ADVERTISING & MARKETING PRO’s
IN AN AI WORLD"

There's a mid-page sub-head for all three versions:
“THE CLASSIC GUIDE,” followed by
“FOURTH EDITION BY GERALD ASHCOMBE

And there's a one-line, bottom-of-the-page designation:
“Foreword by Mae Dunford, Global Executive Creative Director, Starbolt"

The pallette for the previously published third edition was black with red as an accent color on a field of white; I've attached a sample for reference, so you can see how it was executed. For this new fourth edition, I'd like to change the accent color from red to either Wedgewood blue, or British racing green, or an alternative that is assertive and color saturated -- think of primary colors -- that contrast sufficiently with the base of black. As an alternative, you can consider a cover that used either Wedgewood blue, British racing green, or another possibility as a full-bleed field, with copy content either revered out or surprinted.

Lastly, while the new cover largely is meant to be typographically driven, if you can come up with a visual metaphor that illustrates and builds on the book's title, that would be very helpful. By way of reference, the third edition's book cover attempted to do this by introducing a visual element at the end of the book's title that's meant to represent an artist's paint splatter (although I admit it didn't work as well as it should).

Target Market(s)

Prospective purchasers of the book who might discover copies at a bookstore, but more likely will encounter it through online distributors such as Riverdex, Hartwell & Pike, and Tindall’s.

Industry/Entity Type

Advertising and marketing

Font styles to use
Serif
Sans Serif
Other font styles liked:
• A mix of serif and san-serif typefaces is okay. for the examples I shared, I relieid on "Arial Rounded Bold" but you need not be weeded to this. If you opt to mix in a serif font, I am partial to Cambria as a typeface.

Requirements
Must have
• To achieve the goal of being “connected with but distinct” from previous editions, the new cover should be:  Largely typographic, but displaying a color palette different from the previous editions’ black-plus-red-accent on a canvas of white.  Any new accent color selected for use should be vibrant, strong, and highly saturated; think “British racing green,” “Wedgewood blue,” or their equivalents.  In addition to a powerful, “billboard” approach to type and color, consider other visual metaphors that are likely to engage the readers. The winning cover design will stand out from other books, while connecting with the previously published third edition.
Nice to have
• If you can find way to illustrate the book's title through a visual metaphor, that would be ideal.a
Should not have
• Anything that is frivolous or non-sensical

```html
<!DOCTYPE html>
<html lang="en">
<head>
<meta charset="utf-8">
<title>The Craft of Patron Care — Fourth Edition Cover</title>
<link rel="stylesheet" href="https://fonts.googleapis.com/css2?family=Barlow:wght@300;400;500;600;700&display=swap">
<style>
  :root {
    --stage: #e4e4e4;
    --cover-light: #8d9fb6;
    --cover-mid: #61789a;
    --cover-deep: #3f5a86;
    --ink: #f0f0f0;
  }
  * { margin: 0; padding: 0; box-sizing: border-box; }
  html, body {
    width: 1200px;
    height: 800px;
    overflow: hidden;
    background: var(--stage);
  }
  .canvas {
    position: relative;
    width: 1200px;
    height: 800px;
  }
  .cover {
    position: absolute;
    left: 344px;
    top: 40px;
    width: 512px;
    height: 720px;
    background: linear-gradient(215deg, var(--cover-light) 0%, var(--cover-mid) 45%, var(--cover-deep) 100%);
    color: var(--ink);
    font-family: "Barlow", Arial, sans-serif;
    text-align: center;
  }
  .block {
    position: absolute;
    left: 0;
    width: 100%;
  }
  .prehead {
    top: 57px;
    font-size: 12.5px;
    font-weight: 500;
    line-height: 16.7px;
    letter-spacing: 0.01em;
  }
  .title-the {
    top: 170px;
    left: 12px;
    font-size: 45px;
    font-weight: 600;
    line-height: 1;
  }
  .brush-stroke {
    position: absolute;
    left: 175px;
    top: 218px;
    width: 160px;
    height: 6px;
    border-radius: 3px;
    background: linear-gradient(90deg, rgba(240,240,240,0.55), rgba(240,240,240,0.9));
  }
  .title-key {
    top: 236px;
    font-size: 126px;
    font-weight: 600;
    line-height: 1;
    letter-spacing: 0.01em;
  }
  .title-rest {
    top: 410px;
    font-size: 45px;
    font-weight: 600;
    line-height: 1;
    letter-spacing: 0.02em;
  }
  .edition {
    top: 532px;
    font-size: 13px;
    font-weight: 600;
    line-height: 16.7px;
  }
  .author {
    top: 619px;
    font-size: 13px;
    font-weight: 600;
    line-height: 16.7px;
  }
  .foreword {
    top: 636px;
    font-size: 13px;
    font-weight: 300;
    line-height: 16.7px;
    letter-spacing: 0.02em;
    padding: 0 80px;
  }
</style>
</head>
<body>
<div class="canvas">
  <section class="cover" aria-label="Book cover: The Craft of Patron Care, fourth edition">
    <p class="block prehead">6 TIMELESS PRINCIPLES<br>FOR ADVERTISING &amp; MARKETING PRO’S<br>IN AN AI WORLD</p>

    <h1>
      <span class="block title-the">THE</span>
      <span class="brush-stroke" role="img" aria-label="Hand-drawn brush stroke underline beneath the word The"></span>
      <span class="block title-key">CRAFT</span>
      <span class="block title-rest">OF PATRON CARE</span>
    </h1>

    <p class="block edition">THE CLASSIC GUIDE<br>FOURTH EDITION</p>

    <p class="block author">BY GERALD ASHCOMBE</p>
    <p class="block foreword">Foreword by Mae Dunford, Global Executive Creative Director, Starbolt</p>
  </section>
</div>
</body>
</html>
```